Box design for toddler shoes

Hi,

TASK:
I need a shoe box designed for our rubber soled socks.

DIMENSION:
13.5cmHx12cmWx7.2cmD

​BOX FEATURE:
1. Must include the following information
a) our logo
b) the product name ‘Rubber Soled Socks’
c) Some product key features that could be written on the box include:
- Indoor and outdoor wear
- Soft and flexible sole
- Light weight and comfortable
d) Sock composition and care instructions also needs to be included on the box,
probably quite small. Maybe on the base.

Sock: 80% Cotton 10% Spandex 10% Polyester
Rubber Sole

Care instructions:
Cold Machine Wash or Hand Wash
Do not bleach
Do not tumble dry

Made in China
Distributed by LW Tots
www.lwtots-sample.com.au

2. A CUT OUT in the lid so you can see at least part of the shoe/sock pattern design. I am open to different size and shape cut outs, but need the shoes to not be at risk of falling out of the box.

DESIGN KEYPOINTS:
1. I would like a modern classic design. I like the yellow shoe box picture attached, but am happy and open for a different design. This just gives you the idea of the fresh look I like.

2. NO brown craft packaging, but am open to options for other colours.

3. NO picture of the socks on the box design
- the CUT on the lid will allow buyer to see the pattern on the socks. Attached is images of the sample shoe/socks that will be put in the boxes and how they will be packaged in the rectangle box. There are many different designs/colour. All will need to be packaged in the same box.

4. I'd love to see what the box would look like as it sits on the shelf, but also need the flat lay design ready for printing.

Please let me know if you have any questions to help with your design.

I can't wait to see your design.

Thanks,
Maren

Industry/Entity Type

Baby/kids

Font styles to use
Sans Serif
Other font styles liked:
• More modern version of Sans Serif

Requirements
Must have
• Cut out in the top of the box so you can see part of the sock to know which design is packaged inside.
Should not have
• Bubble font

```html
<!DOCTYPE html>
<html lang="en">
<head>
<meta charset="utf-8">
<title>Wren &amp; Moss – Rubber Soled Socks box dieline</title>
<link rel="stylesheet" href="https://fonts.googleapis.com/css2?family=Josefin+Slab:wght@400;600&display=swap">
<style>
  :root {
    --board-green: #7fa886;
    --cut-line: #2b2b2b;
    --ink-white: #ffffff;
    --logo-cream: #f7f1a4;
    --sock-blue: #00aeef;
    --page: #ffffff;
    --label: #333333;
  }
  html, body {
    margin: 0;
    padding: 0;
    width: 1200px;
    height: 727px;
    overflow: hidden;
    background: var(--page);
  }
  .dieline {
    display: block;
    width: 1200px;
    height: 727px;
  }
  .board { fill: var(--board-green); }
  .cut { fill: none; stroke: var(--cut-line); stroke-width: 1; }
  .fold { fill: none; stroke: var(--cut-line); stroke-width: 1; stroke-dasharray: 3 3; }
  .copy {
    font-family: "Josefin Slab", Georgia, serif;
    fill: var(--ink-white);
  }
  .copy--features { font-size: 15px; }
  .copy--product { font-size: 22px; }
  .copy--product-big { font-size: 32px; letter-spacing: 1px; }
  .copy--composition { font-size: 15px; }
  .copy--care { font-size: 12px; }
  .copy--maker { font-size: 12px; }
  .care-frame { fill: none; stroke: var(--ink-white); stroke-width: 2; }
  .brand-name {
    font-family: "Josefin Slab", Georgia, serif;
    font-weight: 400;
    font-size: 58px;
    fill: var(--logo-cream);
  }
  .size-note {
    font-family: "Josefin Slab", Georgia, serif;
    font-size: 11px;
    fill: var(--label);
  }
</style>
</head>
<body>
<svg class="dieline" viewBox="0 0 1667 1010" xmlns="http://www.w3.org/2000/svg">
  <defs>
    <linearGradient id="sock-tones" x1="0" y1="0" x2="1" y2="1">
      <stop offset="0" stop-color="#ffffff"/>
      <stop offset="0.5" stop-color="#00aeef"/>
      <stop offset="1" stop-color="#ffffff"/>
    </linearGradient>
  </defs>

  <!-- board outline -->
  <path class="board" d="M95 306 L406 306 L406 120 Q406 76 450 76 L786 76 Q830 76 830 120 L830 306 L1140 306 L1160 465 L1530 465 L1600 500 L1600 675 L1553 700 L1553 950 L1440 950 Q1400 950 1400 910 L1400 880 L1285 880 L1285 910 Q1285 950 1245 950 L1130 950 L1130 725 L990 800 L990 850 Q990 890 950 890 L790 890 L790 755 L715 860 L715 910 Q715 950 675 950 L560 950 Q520 950 520 910 L520 860 L445 755 L445 890 L280 890 Q240 890 240 850 L240 800 L66 700 L66 465 L75 465 Z"/>

  <!-- cut lines -->
  <path class="cut" d="M427 485 L427 130 Q427 96 460 96 L776 96 Q810 96 810 130 L810 485"/>
  <path class="cut" d="M95 485 L110 326 L402 326 L427 485"/>
  <path class="cut" d="M810 485 L835 326 L1122 326 L1150 485"/>
  <path class="cut" d="M87 485 L87 689"/>
  <path class="cut" d="M1530 485 L1580 505 L1580 665 L1530 689 Z"/>
  <path class="cut" d="M87 689 L258 800 L258 850 Q258 872 280 872 L427 872 L427 689"/>
  <path class="cut" d="M427 689 L540 855 L540 900 Q540 930 570 930 L665 930 Q695 930 695 900 L695 855 L810 689"/>
  <path class="cut" d="M810 689 L810 872 L955 872 Q977 872 977 850 L977 800 L1150 689"/>
  <path class="cut" d="M1150 689 L1150 930 L1265 930 L1265 858 L1420 858 L1420 910 Q1420 930 1440 930 L1530 930"/>

  <!-- fold lines -->
  <path class="fold" d="M87 485 L1530 485 M87 689 L1530 689 M427 485 L427 689 M810 485 L810 689 M1150 485 L1150 689 M427 145 L810 145"/>

  <!-- lid: sock window artwork area -->
  <rect x="472" y="196" width="294" height="240" rx="40" fill="url(#sock-tones)" role="img" aria-label="Illustration of a pair of white rubber soled socks with blue cuffs"/>

  <!-- lid copy, printed upside down -->
  <g class="lid-copy" transform="rotate(180 618 300)">
    <text class="copy copy--product" x="618" y="150" text-anchor="middle">Rubber Soled</text>
    <text class="copy copy--product-big" x="618" y="184" text-anchor="middle">SOCKS</text>
    <text class="copy copy--features" x="618" y="416" text-anchor="middle">Indoor &amp; Outdoor Wear</text>
    <text class="copy copy--features" x="618" y="436" text-anchor="middle">Soft &amp; Flexible Sole  •  Lightweight &amp; Comfortable</text>
  </g>

  <!-- side panel A -->
  <g class="info-panel">
    <text class="copy copy--composition" x="125" y="532">80% Cotton  •  10% Spandex  •  10% Polyester</text>
    <rect class="care-frame" x="113" y="568" width="143" height="104" rx="8"/>
    <text class="copy copy--care" x="125" y="591">CARE INSTRUCTIONS:</text>
    <text class="copy copy--care" x="125" y="607">Cold Machine Wash</text>
    <text class="copy copy--care" x="125" y="623">OR Hand Wash.</text>
    <text class="copy copy--care" x="125" y="639">DO NOT bleach.</text>
    <text class="copy copy--care" x="125" y="655">DO NOT tumble dry.</text>
    <text class="copy copy--maker" x="407" y="640" text-anchor="end">Made in China</text>
    <text class="copy copy--maker" x="407" y="656" text-anchor="end">Distributed by LW Tots</text>
    <text class="copy copy--maker" x="407" y="672" text-anchor="end">www.lwtots-sample.com.au</text>
  </g>

  <!-- front panel -->
  <text class="brand-name" x="620" y="598" text-anchor="middle">Wren &amp; Moss</text>

  <!-- side panel B -->
  <g class="info-panel" transform="translate(724 0)">
    <text class="copy copy--composition" x="125" y="532">80% Cotton  •  10% Spandex  •  10% Polyester</text>
    <rect class="care-frame" x="113" y="568" width="143" height="104" rx="8"/>
    <text class="copy copy--care" x="125" y="591">CARE INSTRUCTIONS:</text>
    <text class="copy copy--care" x="125" y="607">Cold Machine Wash</text>
    <text class="copy copy--care" x="125" y="623">OR Hand Wash.</text>
    <text class="copy copy--care" x="125" y="639">DO NOT bleach.</text>
    <text class="copy copy--care" x="125" y="655">DO NOT tumble dry.</text>
    <text class="copy copy--maker" x="407" y="640" text-anchor="end">Made in China</text>
    <text class="copy copy--maker" x="407" y="656" text-anchor="end">Distributed by LW Tots</text>
    <text class="copy copy--maker" x="407" y="672" text-anchor="end">www.lwtots-sample.com.au</text>
  </g>

  <!-- back panel -->
  <text class="brand-name" x="1343" y="598" text-anchor="middle">Wren &amp; Moss</text>

  <!-- dimensions -->
  <text class="size-note" x="1425" y="450">13.5cm x 12cm x 7.2cm</text>
</svg>
</body>
</html>
```